Business Card desgin, company called Stand Fast.

I am looking for the logo colors (3) to be used on the card in whatever design you think might work. the certifications are on the back (4) on the front will be my name, Dana Whitlock, owner/instructor, phone 208.555.0193, website www.sfx-drills.example, email dw@sfx-drills.example. im flexible on fonts.

Target Market(s)

firearms owners

Industry/Entity Type

firearms training

Contact Information for Business Card

certification icons on back

```html
<!DOCTYPE html>
<html lang="en">
<head>
<meta charset="utf-8">
<title>Stand Fast — Business Card</title>
<link rel="stylesheet" href="https://fonts.googleapis.com/css2?family=Montserrat:wght@400;500;600;700;800&display=swap">
<style>
  :root {
    --board-navy: #012f55;
    --card-navy: #1f2b46;
    --brand-red: #d0112b;
    --paper: #f7f7f5;
    --ink-white: #ffffff;
    --panel-grey: #dcdcdc;
    --badge-grey: #c9ccd3;
  }
  * { margin: 0; padding: 0; box-sizing: border-box; }
  html, body { width: 763px; height: 1200px; overflow: hidden; }
  body {
    background: var(--board-navy);
    font-family: "Montserrat", sans-serif;
    position: relative;
  }

  .showcase-panel {
    position: absolute;
    left: 69px;
    width: 618px;
    height: 410px;
    background: var(--panel-grey);
  }
  .showcase-panel--front { top: 85px; }
  .showcase-panel--back { top: 565px; }

  .card {
    position: absolute;
    left: 89px;
    top: 79px;
    width: 440px;
    height: 252px;
    background: var(--paper);
    box-shadow: 0 2px 6px rgba(0,0,0,.2);
  }

  /* Brand lockup: plain circle + name */
  .brand-lockup { display: flex; align-items: center; }
  .brand-lockup__dot { flex: none; border-radius: 50%; }
  .brand-lockup__name {
    font-weight: 800;
    color: var(--brand-red);
    text-transform: uppercase;
    line-height: 0.95;
  }

  /* Card front */
  .card-front { padding: 22px; }
  .card-front__field {
    position: relative;
    width: 100%;
    height: 100%;
    background: var(--card-navy);
    color: var(--ink-white);
  }
  .card-front .brand-lockup {
    position: absolute;
    left: 18px;
    top: 18px;
    gap: 8px;
  }
  .card-front .brand-lockup__dot {
    width: 40px; height: 40px;
    border: 3px solid var(--ink-white);
  }
  .card-front .brand-lockup__name { font-size: 19px; }
  .card-front__name {
    position: absolute;
    left: 18px;
    top: 112px;
    font-size: 23px;
    font-weight: 700;
  }
  .card-front__role {
    position: absolute;
    left: 18px;
    top: 143px;
    font-size: 11px;
    font-weight: 400;
    letter-spacing: .3px;
  }
  .card-front__contact {
    position: absolute;
    left: 18px;
    top: 166px;
    display: grid;
    grid-template-columns: 46px auto;
    row-gap: 6px;
    font-size: 8.5px;
    letter-spacing: 1px;
  }
  .card-front__web {
    position: absolute;
    right: 14px;
    top: 0;
    bottom: 0;
    writing-mode: vertical-rl;
    transform: rotate(180deg);
    text-align: center;
    font-size: 10px;
    font-weight: 500;
    letter-spacing: .4px;
  }

  /* Card back */
  .card-back { text-align: center; padding-top: 40px; }
  .card-back .brand-lockup { justify-content: center; gap: 12px; }
  .card-back .brand-lockup__dot {
    width: 62px; height: 62px;
    border: 5px solid var(--card-navy);
  }
  .card-back .brand-lockup__name { font-size: 36px; text-align: left; }
  .card-back__label {
    margin-top: 16px;
    font-size: 6.5px;
    font-weight: 500;
    color: var(--card-navy);
    letter-spacing: .3px;
  }
  .cert-row {
    display: flex;
    justify-content: center;
    gap: 14px;
    margin-top: 7px;
  }
  .cert-badge {
    width: 44px; height: 44px;
    border-radius: 50%;
    background: var(--badge-grey);
  }
  .card-back__web {
    margin-top: 14px;
    font-size: 11px;
    font-weight: 600;
    color: var(--card-navy);
    letter-spacing: .3px;
  }

  /* Board footer */
  .board-brand {
    position: absolute;
    left: 70px;
    top: 1036px;
    gap: 14px;
  }
  .board-brand .brand-lockup__dot {
    width: 104px; height: 104px;
    border: 5px solid var(--ink-white);
  }
  .board-brand .brand-lockup__name { font-size: 50px; line-height: 0.98; }
  .board-web {
    position: absolute;
    right: 78px;
    top: 1119px;
    font-size: 13px;
    font-weight: 600;
    color: var(--ink-white);
    letter-spacing: .3px;
  }
</style>
</head>
<body>

  <section class="showcase-panel showcase-panel--front">
    <article class="card card-front">
      <div class="card-front__field">
        <div class="brand-lockup">
          <span class="brand-lockup__dot"></span>
          <span class="brand-lockup__name">Stand<br>Fast</span>
        </div>
        <h1 class="card-front__name">Dana Whitlock</h1>
        <p class="card-front__role">OWNER/INSTRUCTOR</p>
        <dl class="card-front__contact">
          <dt>PHONE:</dt><dd>208.555.0193</dd>
          <dt>EMAIL:</dt><dd>dw@sfx-drills.example</dd>
        </dl>
        <p class="card-front__web">WWW.SFX-DRILLS.EXAMPLE</p>
      </div>
    </article>
  </section>

  <section class="showcase-panel showcase-panel--back">
    <article class="card card-back">
      <div class="brand-lockup">
        <span class="brand-lockup__dot"></span>
        <span class="brand-lockup__name">Stand<br>Fast</span>
      </div>
      <p class="card-back__label">CERTIFICATIONS</p>
      <div class="cert-row">
        <span class="cert-badge" role="img" aria-label="Certification badge"></span>
        <span class="cert-badge" role="img" aria-label="Certification badge"></span>
        <span class="cert-badge" role="img" aria-label="Certification badge"></span>
        <span class="cert-badge" role="img" aria-label="Certification badge"></span>
      </div>
      <p class="card-back__web">WWW.SFX-DRILLS.EXAMPLE</p>
    </article>
  </section>

  <div class="board-brand brand-lockup">
    <span class="brand-lockup__dot"></span>
    <span class="brand-lockup__name">Stand<br>Fast</span>
  </div>
  <p class="board-web">WWW.SFX-DRILLS.EXAMPLE</p>

</body>
</html>
```